Morvell Agronomics, Inc. Business Card

We are joint venture hybrid vegetable seed company. We design & breed application specific products for fresh market and processing applications. We are looking for a business card that will have impact and convey elegance, excellence, high technology, and have enormous eye appeal. It needs to be unique in design and can incorporate photos, or symbols as the case may be.

I very much enjoy the minimalist approach to Quorin's product designs. We would like to include a tag line in the business card: Breeding Success

Target Market(s)

We breed proprietary products that provide better solutions for growers, harvesters, packers, shippers, wholesalers, retailers, consumers, and processors. Regional seed distributors worldwide are our primary clients and then growers. We need to appeal first and foremost to the distributors who will be representing us and selling the products in their target markets.

Industry/Entity Type

Business

Requirements
Must have
• It will have a picture of a cluster of tomatoes on one side and the other side will include the logo, a tag line, our contact information, and a possibly a picture or symbol. I want the contact side to be edgy and convey elegance, solidity, and exclusivity.
Nice to have
• Surprise us with something special.
Should not have
• Card needs to work well with the green logo so it can't be diminished by the background color of the card.

```html
<!DOCTYPE html>
<html lang="en">
<head>
<meta charset="utf-8">
<title>Morvell Agronomics, Inc. Business Card</title>
<link rel="stylesheet" href="https://fonts.googleapis.com/css2?family=Exo+2:wght@400;500;600&display=swap">
<style>
  :root {
    --page-bg: #e9e7e3;
    --card-white: #f7f7f7;
    --panel-dark: #3b3b3c;
    --panel-mid: #5b5b5c;
    --brand-green: #12805c;
    --name-grey: #3a3a3a;
    --tagline-grey: #6a6a6a;
    --text-light: #ffffff;
    --tomato-red: #c8321f;
    --tomato-deep: #7d1a10;
    --vine-green: #3f6b2a;
  }
  * { margin: 0; padding: 0; box-sizing: border-box; }
  html, body {
    width: 1200px; height: 1085px; overflow: hidden;
    background: var(--page-bg);
    font-family: "Exo 2", sans-serif;
  }
  .card-slot {
    position: absolute; left: 170px;
    width: 860px; height: 489px;
  }
  .card-slot.front-slot { top: 38px; }
  .card-slot.back-slot { top: 558px; }
  .card {
    position: absolute; left: 0; top: 0;
    width: 1020px; height: 580px;
    transform: scale(0.8431);
    transform-origin: 0 0;
    background: var(--card-white);
    box-shadow: 0 14px 40px rgba(0,0,0,.18);
    overflow: hidden;
  }
  .card-art { position: absolute; inset: 0; }
  .contact-list {
    position: absolute; left: 0; top: 0; width: 490px; height: 580px;
    color: var(--text-light); text-align: right;
    font-size: 26px; line-height: 34px; letter-spacing: 1px;
  }
  .contact-item { position: absolute; right: 0; white-space: nowrap; }
  .contact-phone { top: 118px; }
  .contact-address { top: 240px; }
  .contact-web { top: 396px; }
  .brand-block {
    position: absolute; left: 640px; top: 130px; width: 360px;
  }
  .brand-name {
    display: flex; align-items: center; gap: 12px;
    color: var(--brand-green); font-weight: 600; font-size: 27px;
    white-space: nowrap;
  }
  .brand-dot {
    width: 22px; height: 22px; border-radius: 50%;
    background: var(--brand-green); flex: none;
  }
  .tagline {
    margin: 10px 0 0 34px;
    color: var(--tagline-grey); font-size: 20px; font-weight: 400;
    letter-spacing: 4px; text-transform: uppercase;
  }
  .person { margin-top: 100px; }
  .person-name {
    color: var(--name-grey); font-size: 34px; font-weight: 500;
    letter-spacing: 3px;
  }
  .person-title {
    color: var(--brand-green); font-size: 28px; font-weight: 500;
    letter-spacing: 1px; margin-top: 4px;
  }
  .tomato-photo {
    position: absolute; inset: 0;
    background:
      radial-gradient(circle at 38% 55%, var(--tomato-red) 0, var(--tomato-deep) 38%, transparent 62%),
      radial-gradient(circle at 66% 42%, var(--tomato-red) 0, var(--tomato-deep) 30%, transparent 55%),
      linear-gradient(160deg, var(--vine-green), #1d3315);
  }
</style>
</head>
<body>
  <div class="card-slot front-slot">
    <div class="card contact-side">
      <svg class="card-art" width="1020" height="580" viewBox="0 0 1020 580">
        <defs>
          <radialGradient id="panelShade" cx="40%" cy="50%" r="65%">
            <stop offset="0" stop-color="#5b5b5c"/>
            <stop offset="1" stop-color="#3b3b3c"/>
          </radialGradient>
        </defs>
        <path class="contact-panel" fill="url(#panelShade)"
          d="M0 0 H500 C500 70 605 90 605 150 C605 200 525 195 525 220
             C525 245 605 240 605 290 C605 340 525 335 525 360
             C525 385 605 380 605 430 C605 500 500 500 500 580 H0 Z"/>
        <g class="contact-icons" fill="none" stroke="#12805c" stroke-width="3">
          <circle cx="563" cy="150" r="24"/>
          <circle cx="563" cy="290" r="24"/>
          <circle cx="563" cy="430" r="24"/>
        </g>
        <g class="icon-glyphs" fill="#12805c">
          <path d="M553 140 q-4 4 0 10 q6 10 16 16 q6 4 10 0 l-5 -5 q-3 3 -6 0 q-6 -5 -10 -10 q-3 -3 0 -6 z"/>
          <path d="M563 276 a9 9 0 0 1 9 9 c0 7 -9 18 -9 18 s-9 -11 -9 -18 a9 9 0 0 1 9 -9 z M563 281 a4 4 0 1 0 0.01 0 z" fill-rule="evenodd"/>
        </g>
        <g class="globe-glyph" fill="none" stroke="#12805c" stroke-width="2">
          <circle cx="563" cy="430" r="12"/>
          <ellipse cx="563" cy="430" rx="5" ry="12"/>
          <line x1="551" y1="430" x2="575" y2="430"/>
          <line x1="553" y1="423" x2="573" y2="423"/>
          <line x1="553" y1="437" x2="573" y2="437"/>
        </g>
      </svg>

      <div class="contact-list">
        <div class="contact-item contact-phone">014 772 3051<br>014 772 3051</div>
        <div class="contact-item contact-address">207, 12th floor,<br>Harlow Crest Road<br>KTR</div>
        <div class="contact-item contact-web">hello@morvellagro.com<br>morvellagro.com</div>
      </div>

      <div class="brand-block">
        <div class="brand-name"><span class="brand-dot"></span>Morvell Agronomics, Inc.</div>
        <div class="tagline">Breeding Success</div>
        <div class="person">
          <div class="person-name">ROWAN ESTEVE</div>
          <div class="person-title">Managing Director</div>
        </div>
      </div>
    </div>
  </div>

  <div class="card-slot back-slot">
    <div class="card tomato-side">
      <div class="tomato-photo" role="img" aria-label="Photograph of a cluster of ripe red tomatoes on the vine"></div>
    </div>
  </div>
</body>
</html>
```